Larkmoor Capital - Financial Planning Solutions

Larkmoor Capital is a financial planning business in Melbourne, Australia. We cater to all kinds of clients from high net worth individuals to young people just starting a career. We need a chart, which will be included in client pitches, presentations and on our website, that conveys the various areas that we are able to provide client solutions.
We have attached three rudimentary interpretations of what we're talking about, one of which includes our logo. With each area of advice we have included a brief description of what it is. The different areas are not necessarily linked, so it's not a circular process but there is a logical progression to them: clients can ask us to get involved with any of the steps.
We are pretty open to suggestions as to the best presentation but are quite interested in an infographics approach.
You can check out our website at www.larkmoorcapital.com.au to see a bit about us, but please be aware that we are changing our investment philosophy and the tone of the website to a broader appeal.
Cheers, Oliver

```html
<!DOCTYPE html>
<html lang="en">
<head>
<meta charset="utf-8">
<title>Larkmoor Capital – Areas of Advice</title>
<link rel="stylesheet" href="https://fonts.googleapis.com/css2?family=Montserrat:wght@300&family=Tinos:wght@400;700&display=swap">
<style>
  :root {
    --page-left: #ddd6c0;
    --page-right: #f8f7f3;
    --panel-left: #eeebe2;
    --panel-right: #fbfbf9;
    --frame: #111111;
    --tile: #c7bf9d;
    --ink: #141414;
    --brand-ink: #2a2a2a;
  }
  * { margin: 0; padding: 0; box-sizing: border-box; }
  html, body { width: 1200px; height: 900px; overflow: hidden; }
  body {
    position: relative;
    background: linear-gradient(90deg, var(--page-left), var(--page-right));
    font-family: "Tinos", "Times New Roman", serif;
    color: var(--ink);
  }
  .frame {
    position: absolute;
    left: 26px; top: 29px; width: 1151px; height: 841px;
    border: 27px solid var(--frame);
    border-top: none;
    background: linear-gradient(90deg, var(--panel-left), var(--panel-right));
  }
  .frame-top {
    position: absolute;
    top: 29px; height: 27px;
    background: var(--frame);
  }
  .frame-top--left { left: 26px; width: 510px; }
  .frame-top--right { left: 668px; width: 509px; }

  .brand {
    position: absolute;
    left: 0; width: 1200px; top: 94px;
    text-align: center;
    font-family: "Montserrat", "Helvetica Neue", sans-serif;
    font-weight: 300;
    color: var(--brand-ink);
  }
  .brand-name { display: block; font-size: 35px; letter-spacing: 5px; line-height: 36px; }
  .brand-sub { display: block; font-size: 20px; letter-spacing: 7px; line-height: 26px; margin-top: 2px; }

  .service-title {
    position: absolute;
    display: flex; align-items: center; justify-content: center;
    height: 59px;
    background: var(--tile);
    font-weight: 700;
    font-size: 22px;
    line-height: 27px;
    letter-spacing: 0.3px;
    text-align: center;
  }
  .service-desc {
    position: absolute;
    width: 380px;
    font-size: 17.5px;
    line-height: 23.5px;
    text-align: center;
  }

  .income    .service-title { left: 485px; top: 244px; width: 262px; }
  .income    .service-desc  { left: 426px; top: 310px; }
  .estate    .service-title { left: 177px; top: 339px; width: 236px; }
  .estate    .service-desc  { left: 102px; top: 405px; }
  .tax       .service-title { left: 839px; top: 339px; width: 236px; }
  .tax       .service-desc  { left: 767px; top: 405px; }
  .insurance .service-title { left: 113px; top: 472px; width: 236px; }
  .insurance .service-desc  { left: 44px;  top: 539px; }
  .planning  .service-title { left: 890px; top: 472px; width: 235px; }
  .planning  .service-desc  { left: 784px; top: 539px; }
  .portfolio .service-title { left: 268px; top: 602px; width: 236px; }
  .portfolio .service-desc  { left: 183px; top: 669px; }
  .debt      .service-title { left: 721px; top: 602px; width: 235px; }
  .debt      .service-desc  { left: 637px; top: 669px; width: 380px; }
  .super     .service-title { left: 485px; top: 717px; width: 262px; }
  .super     .service-desc  { left: 426px; top: 784px; }
</style>
</head>
<body>
  <div class="frame"></div>
  <div class="frame-top frame-top--left"></div>
  <div class="frame-top frame-top--right"></div>

  <header class="brand">
    <span class="brand-name">LARKMOOR</span>
    <span class="brand-sub">CAPITAL</span>
  </header>

  <main class="services">
    <section class="service income">
      <h2 class="service-title">HOUSEHOLD<br>INCOME</h2>
      <p class="service-desc">Funds earned from work or investments</p>
    </section>
    <section class="service estate">
      <h2 class="service-title">ESTATE<br>PLANNING</h2>
      <p class="service-desc">Ensure your assets are dealt with as you<br>want</p>
    </section>
    <section class="service tax">
      <h2 class="service-title">TAX<br>ADVICE</h2>
      <p class="service-desc">Maximize after tax income</p>
    </section>
    <section class="service insurance">
      <h2 class="service-title">INSURANCE</h2>
      <p class="service-desc">Protect the lifestyle you’ve built for you<br>and your family.</p>
    </section>
    <section class="service planning">
      <h2 class="service-title">FINANCIAL<br>PLANNING</h2>
      <p class="service-desc">A road map for the application of your<br>after tax income</p>
    </section>
    <section class="service portfolio">
      <h2 class="service-title">INVESTMENT<br>PORTFOLIO</h2>
      <p class="service-desc">Optimize the return on your tax income</p>
    </section>
    <section class="service debt">
      <h2 class="service-title">DEBT</h2>
      <p class="service-desc">To fund the purchase of a house of other asset</p>
    </section>
    <section class="service super">
      <h2 class="service-title">SUPERANNUATION</h2>
      <p class="service-desc">Advice on structuring and management</p>
    </section>
  </main>
</body>
</html>
```